Korvane Works Business cards

We require somebody to design business cards for our new business.

Target Market(s)

Mining, haulage and civil.

Industry/Entity Type

Auto electrician in mining industry

Contact Information for Business Card

ABN, business email address, mobile number.

Colors
00AB8E
00BBA5
67D7C9
C6EFE9
E9F9F6

Requirements
Must have
• Services I offer: Breakdowns, Field Service, A/C Systems, Machine rewires, mine site vehicle fit outs

```html
<!DOCTYPE html>
<html lang="en">
<head>
<meta charset="utf-8">
<title>Korvane Works Business Cards</title>
<link rel="stylesheet" href="https://fonts.googleapis.com/css2?family=Montserrat:wght@400;500;700&display=swap">
<style>
  :root {
    --backdrop: #9a9a9a;
    --card: #1a1a1a;
    --teal: #5ccbc1;
    --teal-deep: #3fb3a8;
    --silver: #b9b9b9;
    --text: #f1f1f1;
    --art-top: #4aa9a1;
    --art-bottom: #2f6f6a;
  }
  * { box-sizing: border-box; margin: 0; padding: 0; }
  html, body { width: 1200px; height: 1108px; overflow: hidden; }
  body {
    background: var(--backdrop);
    font-family: "Montserrat", Arial, sans-serif;
    position: relative;
  }
  .card {
    position: absolute;
    left: 240px;
    width: 717px;
    height: 411px;
    background: var(--card);
    border-radius: 30px;
    border-left: 3px solid var(--teal);
    border-bottom: 3px solid var(--teal);
    overflow: hidden;
  }
  .card-front { top: 119px; }
  .card-back { top: 580px; }

  .artwork {
    position: absolute;
    border-radius: 6px;
    background: linear-gradient(180deg, var(--art-top), var(--art-bottom));
  }
  .rule {
    position: absolute;
    height: 3px;
    background: linear-gradient(90deg, transparent, var(--silver) 8%, var(--silver) 92%, transparent);
  }
  .brand-name {
    position: absolute;
    font-weight: 700;
    color: var(--teal);
    text-align: center;
    white-space: nowrap;
  }

  /* front */
  .card-front .rig-art { left: 300px; top: 64px; width: 150px; height: 128px; }
  .card-front .rule-top { left: 232px; top: 195px; width: 252px; }
  .card-front .brand-name { left: 200px; width: 317px; top: 204px; font-size: 38px; }
  .card-front .rule-bottom { left: 232px; top: 264px; width: 252px; }
  .card-front .truck-art { left: 232px; top: 270px; width: 205px; height: 76px; }

  /* back */
  .card-back .rig-art { left: 82px; top: 26px; width: 112px; height: 118px; }
  .card-back .rule-top { left: 27px; top: 146px; width: 200px; }
  .card-back .brand-name { left: 14px; width: 226px; top: 152px; font-size: 27px; }
  .card-back .rule-bottom { left: 27px; top: 193px; width: 200px; }
  .card-back .truck-art { left: 27px; top: 198px; width: 162px; height: 50px; }

  .contact-list { position: absolute; left: 27px; top: 300px; list-style: none; }
  .contact-list li {
    display: flex; align-items: center; gap: 9px;
    height: 28.5px; font-size: 17.5px; color: var(--text);
  }
  .contact-list svg { width: 16px; height: 16px; fill: var(--teal); flex: none; }

  .abn { position: absolute; left: 297px; top: 363px; font-size: 17.5px; color: var(--text); }

  .services-title {
    position: absolute; right: 30px; top: 190px;
    font-size: 20px; font-weight: 700; color: var(--teal);
  }
  .services-list { position: absolute; right: 30px; top: 234px; list-style: none; text-align: right; }
  .services-list li {
    height: 28.5px; font-size: 17px; color: var(--text); white-space: nowrap;
    display: flex; justify-content: flex-end; align-items: center; gap: 9px;
  }
  .services-list li::after {
    content: ""; width: 8px; height: 8px; border-radius: 50%; background: var(--teal);
    margin-top: 4px; flex: none;
  }
</style>
</head>
<body>

  <section class="card card-front" aria-label="Business card front">
    <div class="artwork rig-art" role="img" aria-label="Illustration of a drill rig mast with a lightning bolt"></div>
    <div class="rule rule-top"></div>
    <div class="brand-name">Korvane Works</div>
    <div class="rule rule-bottom"></div>
    <div class="artwork truck-art" role="img" aria-label="Illustration of a drilling truck"></div>
  </section>

  <section class="card card-back" aria-label="Business card back">
    <div class="artwork rig-art" role="img" aria-label="Illustration of a drill rig mast with a lightning bolt"></div>
    <div class="rule rule-top"></div>
    <div class="brand-name">Korvane Works</div>
    <div class="rule rule-bottom"></div>
    <div class="artwork truck-art" role="img" aria-label="Illustration of a drilling truck"></div>

    <ul class="contact-list">
      <li>
        <svg viewBox="0 0 16 16" aria-hidden="true"><path d="M1 6c0-2 3-3 7-3s7 1 7 3v1h-3V5.5C11 5 9.5 4.8 8 4.8S5 5 4 5.5V7H1z"/><path d="M3 8h10l1 5H2z"/></svg>
        <span>123 456 789</span>
      </li>
      <li>
        <svg viewBox="0 0 16 16" aria-hidden="true"><path d="M1 3h14v10H1z M2.5 4.5 8 9l5.5-4.5" fill="none" stroke="#5ccbc1" stroke-width="1.6"/></svg>
        <span>info@yourgmail.com</span>
      </li>
      <li>
        <svg viewBox="0 0 16 16" aria-hidden="true"><circle cx="8" cy="8" r="7"/><path d="M5 4c2 1 1 3 3 3s1 3-1 4" fill="none" stroke="#1a1a1a" stroke-width="1.4"/></svg>
        <span>www.yourwebsite.com</span>
      </li>
    </ul>

    <div class="abn">ABN# 123 45678</div>

    <h2 class="services-title">Services I offer</h2>
    <ul class="services-list">
      <li>Breakdowns</li>
      <li>Field Service</li>
      <li>A/C Systems</li>
      <li>Machine rewires</li>
      <li>Mine site vehicle fit outs</li>
    </ul>
  </section>

</body>
</html>
```